Business Card for Yachting Management Company

Need a business card design for a new yachting project management company. Attached is the logo for the company.
Our clients are large yacht owners and captains.
Design must be in the style of the logo. Modern, elegant.

Example of data to show:
Peter Hollis
Project Manager
(+34) 612 738 104
peter@quorvane.net
Quorvane Management - Meridel Tower, Office 22 - KRB - Palma de Mallorca

The data above will have to be changed (by me) for the different people in the company over the next years.

Will be printed using PrintNova (Lustre Card Series). They provide these guidelines for the size:
"the actual size of the card is 1050 x 600 pixels. However, the full bleed size is 1083 x 633 pixels, and the safe printing area is 1008 x 558 pixels."

```html
<!DOCTYPE html>
<html lang="en">
<head>
<meta charset="utf-8">
<title>Quorvane Management – Business Card</title>
<link href="https://fonts.googleapis.com/css2?family=Montserrat:wght@400;500;600;700&display=swap" rel="stylesheet">
<style>
  :root {
    --backdrop: #3a3a3c;
    --card-white: #ffffff;
    --card-black: #151516;
    --brand-blue: #0a6fc2;
    --brand-grey: #808080;
    --ink: #1e1e1e;
  }
  * { box-sizing: border-box; margin: 0; padding: 0; }
  html, body { width: 1200px; height: 1200px; overflow: hidden; }
  body {
    background: var(--backdrop);
    font-family: "Montserrat", sans-serif;
    display: flex;
    flex-direction: column;
    align-items: center;
    justify-content: center;
    gap: 60px;
  }
  .card {
    position: relative;
    width: 840px;
    height: 480px;
    border-radius: 34px;
    overflow: hidden;
  }
  .card--front { background: var(--card-white); }
  .card--back {
    background: var(--card-black);
    display: flex;
    align-items: center;
    justify-content: center;
  }

  /* Front: identity block */
  .identity {
    position: absolute;
    left: 70px;
    top: 150px;
    padding-left: 18px;
    border-left: 6px solid var(--brand-blue);
  }
  .identity__name {
    color: var(--brand-blue);
    font-weight: 700;
    font-size: 34px;
    letter-spacing: 0.5px;
    line-height: 1;
    text-transform: uppercase;
  }
  .identity__role {
    color: var(--ink);
    font-weight: 500;
    font-size: 21px;
    margin-top: 4px;
  }

  .contacts {
    position: absolute;
    left: 88px;
    top: 258px;
    list-style: none;
    color: var(--ink);
    font-size: 17px;
    font-weight: 500;
    line-height: 1.25;
  }
  .contacts__item {
    display: flex;
    align-items: flex-start;
    gap: 14px;
    margin-bottom: 8px;
  }
  .contacts__icon {
    width: 20px;
    height: 20px;
    flex: none;
    margin-top: 1px;
    fill: var(--brand-blue);
  }

  /* Front: wordmark */
  .wordmark {
    position: absolute;
    right: 60px;
    top: 150px;
    width: 370px;
    color: var(--brand-blue);
    font-weight: 600;
    font-size: 44px;
    line-height: 1.1;
    text-align: center;
  }

  /* Front: bottom band */
  .band {
    position: absolute;
    left: 0;
    right: 0;
    bottom: 0;
    height: 22px;
    display: flex;
  }
  .band__blue { flex: 0 0 68%; background: var(--brand-blue); }
  .band__grey { flex: 1; background: var(--brand-grey); margin-left: 8px; }

  /* Back: wordmark */
  .wordmark--large {
    color: var(--brand-blue);
    font-weight: 600;
    font-size: 72px;
    line-height: 1.1;
    text-align: center;
  }
</style>
</head>
<body>
  <section class="card card--front" aria-label="Business card front">
    <div class="identity">
      <p class="identity__name">Peter Hollis</p>
      <p class="identity__role">Project Manager</p>
    </div>

    <ul class="contacts">
      <li class="contacts__item">
        <svg class="contacts__icon" viewBox="0 0 24 24" aria-hidden="true"><path d="M6.6 10.8a15.1 15.1 0 0 0 6.6 6.6l2.2-2.2a1 1 0 0 1 1-.25 11.4 11.4 0 0 0 3.6.57 1 1 0 0 1 1 1V20a1 1 0 0 1-1 1A17 17 0 0 1 3 4a1 1 0 0 1 1-1h3.5a1 1 0 0 1 1 1c0 1.25.2 2.45.57 3.57a1 1 0 0 1-.25 1z"/></svg>
        <span>(+34) 612 738 104</span>
      </li>
      <li class="contacts__item">
        <svg class="contacts__icon" viewBox="0 0 24 24" aria-hidden="true"><path d="M2 5h20v14H2z M3.5 6.5 12 13l8.5-6.5" /><path d="M2 5l10 8 10-8v14H2z" fill="none"/></svg>
        <span>peter@quorvane.net</span>
      </li>
      <li class="contacts__item">
        <svg class="contacts__icon" viewBox="0 0 24 24" aria-hidden="true"><path d="M12 2a7 7 0 0 0-7 7c0 5.2 7 13 7 13s7-7.8 7-13a7 7 0 0 0-7-7zm0 9.5A2.5 2.5 0 1 1 12 6.5a2.5 2.5 0 0 1 0 5z"/></svg>
        <span>Quorvane Management - Meridel Tower,<br>Office 22 - KRB - Palma de Mallorca</span>
      </li>
    </ul>

    <p class="wordmark">Quorvane Management</p>

    <div class="band" aria-hidden="true">
      <div class="band__blue"></div>
      <div class="band__grey"></div>
    </div>
  </section>

  <section class="card card--back" aria-label="Business card back">
    <p class="wordmark--large">Quorvane<br>Management</p>
  </section>
</body>
</html>
```